PowerPoint Presentation 10 Slides Needed with custom graphics and possibly animated gifs

I'm creating an educational webinar for professionals. I have 10 slides that need special treatment--effective visuals that really Deliverables10 PowerPoint slides in shared PPT fileWith 10 or more images that communicate the message described in the slides notes for each slide.DeadlineSlides will be used in a PowerPoint presentation Monday, Dec 10.Due date is Friday, Dec 7.Design GuidanceSee attached deck for existing design template/theme (with colors/logo)You should match the designAnimations should be delivered as GIF files that can appear in a slideAnimation can last 4 to 10 seconds.Instead of animations, photos from Pixelvane can be recommended (I have an account and can provide the final file to use).

```html
<!DOCTYPE html>
<html lang="en">
<head>
<meta charset="utf-8">
<title>Commicare Means To Share</title>
<link href="https://fonts.googleapis.com/css2?family=Lato:wght@400;700&display=swap" rel="stylesheet">
<style>
  :root {
    --bg: #ffffff;
    --ink: #111111;
    --title: #5589ae;
    --dot-blue: #4a86e8;
    --dot-green: #00904a;
    --dot-sky: #0b8ce0;
    --dot-mint: #4fd1a0;
    --giver: #00c785;
    --gift: #f27300;
    --recipient: #d44cf5;
    --brand: #1f4e9a;
    --corner: #00904a;
  }
  html, body {
    margin: 0;
    padding: 0;
    overflow: hidden;
    background: var(--bg);
  }
  .slide {
    position: relative;
    width: 1200px;
    height: 675px;
    overflow: hidden;
    background: var(--bg);
    font-family: "Lato", Arial, sans-serif;
    color: var(--ink);
  }
  .slide-title {
    position: absolute;
    top: 52px;
    left: 0;
    width: 1200px;
    margin: 0;
    text-align: center;
    font-size: 38px;
    font-weight: 700;
    color: var(--title);
    letter-spacing: -0.2px;
  }
  .title-dots {
    position: absolute;
    top: 114px;
    left: 563px;
    display: flex;
    gap: 2px;
  }
  .title-dots span {
    width: 13px;
    height: 13px;
    border-radius: 50%;
  }
  .brand {
    position: absolute;
    top: 58px;
    right: 36px;
    display: flex;
    align-items: center;
    gap: 6px;
    font-size: 17px;
    font-weight: 700;
    color: var(--brand);
  }
  .brand-mark {
    width: 12px;
    height: 12px;
    border-radius: 50%;
    background: var(--brand);
  }
  .body-text {
    position: absolute;
    left: 128px;
    margin: 0;
    font-size: 21px;
    line-height: 28px;
  }
  .etymology { top: 210px; }
  .share-list { top: 323px; }
  .share-list .giver { color: var(--giver); }
  .share-list .gift { color: var(--gift); }
  .share-list .recipient { color: var(--recipient); }
  .connection { top: 492px; }
  .exchange-illustration {
    position: absolute;
    left: 570px;
    top: 276px;
    width: 366px;
    height: 198px;
    border-radius: 6px;
    background: linear-gradient(90deg, #bfeedd 0%, #ffd9b8 50%, #f1c6fb 100%);
  }
  .corner-dot {
    position: absolute;
    left: 1145px;
    top: 621px;
    width: 38px;
    height: 38px;
    border-radius: 50%;
    background: var(--corner);
  }
</style>
</head>
<body>
  <main class="slide">
    <h1 class="slide-title">Commicare Means To Share</h1>
    <div class="title-dots" aria-hidden="true">
      <span style="background: var(--dot-blue)"></span>
      <span style="background: var(--dot-green)"></span>
      <span style="background: var(--dot-sky)"></span>
      <span style="background: var(--dot-mint)"></span>
      <span style="background: var(--dot-blue)"></span>
    </div>

    <div class="brand"><span class="brand-mark"></span>Client Ascend</div>

    <p class="body-text etymology">Communication is from late Middle English Old French from the verb communicate ‘to share’</p>

    <p class="body-text share-list">
      To share, there must be at least:<br>
      <span class="giver">1. Giver (you, trying to communicate)</span><br>
      <span class="gift">2. The gift (message)</span><br>
      <span class="recipient">3. Recipient</span>
    </p>

    <div class="exchange-illustration" role="img" aria-label="Two simple figures, a green giver and a purple recipient, with an orange gift box between them"></div>

    <p class="body-text connection">What may be obvious is that there should be some kind of connection.</p>

    <div class="corner-dot" aria-hidden="true"></div>
  </main>
</body>
</html>
```